Harlow Ironworks Business Card

We need a business card design for a new small metal fabrication business in rural NSW, Australia.

The business (Harlow Ironworks) is owner operated by a man with the initials KB - much of the branding comes from this name.

Harlow Ironworks designs, engineers, repairs and manufactures a range of custom, quality metal works including vehicle trays, agricultural machinery impliments, trailers, wood splitters, fire pits, furniture etc.

The brand position focuses on custom work of the highest quality.

Business card design should show quality, attention to detail and stand out among a mass of business cards.

Logos are in the files

The grey color may be changed on the logo if required to stand out more.

There is an image attached of a simple card that is liked because it is clean, clear, simple, masculine and effective. It says 'quality'. As most of the work we do is custom it would be good to have the business card speak to this.

Target Market(s)

Rural and regional based Australians. Primarily adult male 25-60 yrs. Primary production / rural / travelling lifestyle.

Industry/Entity Type

Metal Fabrication

Contact Information for Business Card

The words 'custom quality fabrications' would be great somewhere perhaps on the backside (not on the information side)
Name
title
Phone: 0418 539 746 and (02) 6193 4827
email: info@harlowiw.com.au
www.harlowiw.com.au

address (2 lines)

Requirements
Nice to have
• Background colour should be very navy blue or black.
Should not have
• NO orange and blue combinations.
• Navy is OK

```html
<!DOCTYPE html>
<html lang="en">
<head>
<meta charset="utf-8">
<title>Harlow Ironworks Business Card</title>
<link rel="stylesheet" href="https://fonts.googleapis.com/css2?family=Open+Sans:wght@400;700;800&display=swap">
<style>
  :root {
    --backdrop: #6b4a36;
    --card: #262626;
    --green: #6cc04a;
    --grey: #a6a6a6;
    --text: #cfcfcf;
    --rule: #8a8a8a;
  }
  * { margin: 0; padding: 0; box-sizing: border-box; }
  html, body { width: 1200px; height: 1000px; overflow: hidden; }
  body {
    background: var(--backdrop);
    font-family: "Open Sans", Arial, sans-serif;
    position: relative;
  }
  .card {
    position: absolute;
    left: 266px;
    width: 666px;
    height: 397px;
    background: var(--card);
    box-shadow: 0 3px 10px rgba(0,0,0,0.45);
  }
  .card--front { top: 74px; }
  .card--back { top: 533px; }

  /* Front */
  .front-brand {
    position: absolute;
    left: 44px; top: 112px;
    width: 256px;
    color: var(--grey);
    font-weight: 800;
    font-size: 36px;
    line-height: 1.1;
    letter-spacing: 1px;
    text-transform: uppercase;
  }
  .divider {
    position: absolute;
    left: 344px; top: 96px;
    width: 1px; height: 206px;
    background: var(--rule);
  }
  .details {
    position: absolute;
    left: 387px; top: 90px;
    color: var(--text);
    font-size: 16px;
    line-height: 24px;
  }
  .details__name {
    color: var(--green);
    font-weight: 700;
    font-size: 20px;
    letter-spacing: 0.5px;
    text-transform: uppercase;
    line-height: 26px;
  }
  .details__title { margin-bottom: 14px; }
  .details__address { margin-bottom: 9px; }
  .contact-list { list-style: none; }
  .contact-list li { display: flex; align-items: center; height: 23px; }
  .contact-list svg { width: 13px; height: 13px; margin-right: 7px; fill: var(--green); flex: none; }

  /* Back */
  .back-brand {
    position: absolute;
    left: 0; right: 0; top: 146px;
    display: flex; align-items: center; justify-content: center;
    gap: 22px;
  }
  .back-brand__square {
    width: 64px; height: 64px;
    background: var(--green);
  }
  .back-brand__name {
    color: var(--grey);
    font-weight: 800;
    font-size: 46px;
    letter-spacing: 2px;
    text-transform: uppercase;
  }
  .tagline {
    position: absolute;
    left: 0; right: 0; top: 346px;
    text-align: center;
    color: var(--grey);
    font-size: 17px;
    letter-spacing: 3px;
    text-transform: uppercase;
  }
</style>
</head>
<body>
  <section class="card card--front">
    <div class="front-brand">Harlow<br>Ironworks</div>
    <div class="divider"></div>
    <div class="details">
      <div class="details__name">Kurt Bramwell</div>
      <div class="details__title">Cheif Managing Officer</div>
      <div class="details__address">418 Kestrel Rd, Unit 3<br>Wagga Wagga NSW 2650</div>
      <ul class="contact-list">
        <li><svg viewBox="0 0 16 16"><path d="M1 6c0-2 3-3 7-3s7 1 7 3v1h-4V5.5H5V7H1z M3 8h10l1 6H2z"/></svg>0418 539 746</li>
        <li><svg viewBox="0 0 16 16"><path d="M4 1h8v4H4z M1 6h14v6h-3v-2H4v2H1z M5 11h6v4H5z"/></svg>(02) 6193 4827</li>
        <li><svg viewBox="0 0 16 16"><path d="M1 3h14v1.5L8 9 1 4.5z M1 6.3l7 4.5 7-4.5V13H1z"/></svg>info@harlowiw.com.au</li>
        <li><svg viewBox="0 0 16 16"><circle cx="7" cy="7" r="6"/><path d="M8 8l7 3-3 1-1 3z" fill="#262626" stroke="#6cc04a" stroke-width="1"/></svg>www.harlowiw.com.au</li>
      </ul>
    </div>
  </section>

  <section class="card card--back">
    <div class="back-brand">
      <div class="back-brand__square"></div>
      <div class="back-brand__name">Harlow Ironworks</div>
    </div>
    <div class="tagline">Custom Metal Fabrication</div>
  </section>
</body>
</html>
```